infographic series

To convert each of the below pieces of information into a graphic for facebook.
The 07 figure should be blue and the 2012 figure should be red.
The audience is Australian, female and aged 25-45 with dependent children.
These should be provided both as four separate infographics and as one which includes all three figures.
Early childhood and child care budget
2012 $22.3 billion
2007 $7.3 billion
Hearthward Allowance
2007 $4,354
2012 $7,500
Families using approved child care
2007 571,900
2012 929,000 (62.4% increase)
Approved child care services
2007 11,266
2012 16,000
Target Market(s)
women aged 25-45 with young kids skimming their facebook newsfeed
Look and feel

```html
<!DOCTYPE html>
<html lang="en">
<head>
<meta charset="utf-8">
<title>Child Care Infographic Series</title>
<link rel="stylesheet" href="https://fonts.googleapis.com/css2?family=Alfa+Slab+One&family=Arvo:wght@400;700&display=swap">
<style>
  :root {
    --red: #c8262c;
    --red-deep: #a91f25;
    --blue: #2c62a0;
    --blue-deep: #234f84;
    --ink: #161616;
    --panel-centre: #eef4f8;
    --panel-edge: #b7cdd9;
    --page: #ffffff;
    --wood: #6e4226;
  }
  * { margin: 0; padding: 0; box-sizing: border-box; }
  html, body { width: 1200px; height: 1007px; overflow: hidden; background: var(--page); }
  .board { position: relative; width: 1200px; height: 1007px; font-family: "Arvo", Georgia, serif; }

  .panel {
    position: absolute;
    width: 579px;
    height: 480px;
    border-radius: 28px;
    background: radial-gradient(ellipse at 50% 50%, var(--panel-centre) 0%, #d6e4ec 55%, var(--panel-edge) 100%);
    overflow: hidden;
  }
  .panel--services { left: 13px;  top: 13px; }
  .panel--families { left: 608px; top: 13px; }
  .panel--allowance{ left: 13px;  top: 511px; }
  .panel--budget   { left: 608px; top: 511px; }

  .panel > * { position: absolute; }

  .title {
    font-family: "Arvo", Georgia, serif;
    font-weight: 700;
    font-size: 31px;
    line-height: 46px;
    color: var(--ink);
    letter-spacing: -0.5px;
    white-space: nowrap;
  }
  .title--right { text-align: right; }

  .year, .figure { font-family: "Arvo", Georgia, serif; line-height: 1; white-space: nowrap; }
  .year { font-size: 28px; font-weight: 700; }
  .figure { font-size: 32px; font-weight: 400; }
  .is-2012 { color: var(--red); }
  .is-2007 { color: var(--blue); }

  .change {
    font-family: "Alfa Slab One", Georgia, serif;
    color: var(--red);
    line-height: 1;
    white-space: nowrap;
  }

  .artwork { border-radius: 12px; }

  /* Approved services: a long red row of blocks over a shorter blue row */
  .panel--services .title { left: 20px; top: 32px; }
  .panel--services .year.is-2012 { left: 26px; top: 114px; }
  .panel--services .figure.is-2012 { left: 26px; top: 152px; }
  .panel--services .change { left: 187px; top: 124px; font-size: 62px; }
  .panel--services .year.is-2007 { right: 26px; top: 114px; }
  .panel--services .figure.is-2007 { right: 24px; top: 152px; }
  .panel--services .blocks--2012 {
    left: 66px; top: 262px; width: 450px; height: 64px;
    background: linear-gradient(90deg, var(--wood) 0%, var(--red) 12%, var(--red-deep) 100%);
    transform: rotate(-6deg);
  }
  .panel--services .blocks--2007 {
    left: 70px; top: 372px; width: 316px; height: 62px;
    background: linear-gradient(90deg, var(--wood) 0%, var(--blue) 14%, var(--blue-deep) 100%);
    transform: rotate(-9deg);
  }

  /* Families: a large red family with a smaller blue family in front */
  .panel--families .title { right: 27px; top: 28px; }
  .panel--families .change { left: 10px; top: 72px; font-size: 62px; }
  .panel--families .year.is-2012 { left: 26px; top: 148px; }
  .panel--families .figure.is-2012 { left: 26px; top: 186px; }
  .panel--families .year.is-2007 { right: 42px; top: 148px; }
  .panel--families .figure.is-2007 { right: 40px; top: 186px; }
  .panel--families .family--2012 {
    left: 64px; top: 226px; width: 496px; height: 240px;
    background: var(--red);
    border-radius: 90px 90px 6px 6px;
  }
  .panel--families .family--2007 {
    left: 230px; top: 300px; width: 310px; height: 166px;
    background: var(--blue);
    border: 4px solid #ffffff;
    border-bottom: none;
    border-radius: 60px 60px 0 0;
  }

  /* Allowance */
  .panel--allowance .title { right: 22px; top: 32px; }
  .panel--allowance .items--2012 {
    left: 20px; top: 124px; width: 540px; height: 80px;
    background: linear-gradient(90deg, var(--red-deep), var(--red), var(--red-deep));
    border-radius: 18px;
  }
  .panel--allowance .items--2007 {
    left: 216px; top: 246px; width: 320px; height: 76px;
    background: linear-gradient(90deg, var(--blue-deep), var(--blue), var(--blue-deep));
    border-radius: 18px;
  }
  .panel--allowance .year.is-2012 { left: 26px; top: 246px; }
  .panel--allowance .figure.is-2012 { left: 26px; top: 292px; }
  .panel--allowance .change { left: 22px; top: 366px; font-size: 72px; }
  .panel--allowance .year.is-2007 { left: 336px; top: 362px; }
  .panel--allowance .figure.is-2007 { left: 336px; top: 402px; }

  /* Budget */
  .panel--budget .title { right: 34px; top: 22px; }
  .panel--budget .year { font-size: 20px; }
  .panel--budget .figure { font-size: 24px; }
  .panel--budget .year.is-2012 { left: 214px; top: 152px; }
  .panel--budget .figure.is-2012 { left: 214px; top: 178px; }
  .panel--budget .year.is-2007 { left: 390px; top: 160px; }
  .panel--budget .figure.is-2007 { left: 390px; top: 186px; }
  .panel--budget .baby {
    left: 12px; top: 228px; width: 530px; height: 222px;
    background: linear-gradient(90deg, var(--red) 0%, var(--red) 55%, var(--blue) 55%, var(--blue) 100%);
    border-radius: 90px 40px 40px 60px;
  }
  .panel--budget .change { left: 50px; top: 292px; font-size: 50px; color: #ffffff; }
</style>
</head>
<body>
<main class="board">

  <section class="panel panel--services">
    <h2 class="title">Approved Child Care Services</h2>
    <span class="year is-2012">2012</span>
    <span class="figure is-2012">16,000</span>
    <span class="change">+42%</span>
    <span class="year is-2007">2007</span>
    <span class="figure is-2007">11,266</span>
    <div class="artwork blocks--2012" role="img" aria-label="Row of eight wooden alphabet blocks with red letters spelling APPROVED"></div>
    <div class="artwork blocks--2007" role="img" aria-label="Shorter row of wooden alphabet blocks with blue letters spelling APPROV"></div>
  </section>

  <section class="panel panel--families">
    <h2 class="title title--right">Families Using Approved<br>Child Care</h2>
    <span class="change">+62%</span>
    <span class="year is-2012">2012</span>
    <span class="figure is-2012">929,000</span>
    <span class="year is-2007">2007</span>
    <span class="figure is-2007">571,900</span>
    <div class="artwork family--2012" role="img" aria-label="Silhouettes of a large red family of adults and children"></div>
    <div class="artwork family--2007" role="img" aria-label="Silhouettes of a smaller blue family standing in front"></div>
  </section>

  <section class="panel panel--allowance">
    <h2 class="title title--right">Hearthward Allowance</h2>
    <div class="artwork items--2012" role="img" aria-label="Row of red baby items: bottles, teddy bears, spoons and cups"></div>
    <div class="artwork items--2007" role="img" aria-label="Shorter row of blue baby items: cup, bottle, teddy bear, spoon and cup"></div>
    <span class="year is-2012">2012</span>
    <span class="figure is-2012">$7,500</span>
    <span class="change">+72%</span>
    <span class="year is-2007">2007</span>
    <span class="figure is-2007">$4,354</span>
  </section>

  <section class="panel panel--budget">
    <h2 class="title title--right">Early Childhood<br>&amp; Child Care Budget</h2>
    <span class="year is-2012">2012</span>
    <span class="figure is-2012">$22.3 billion</span>
    <span class="year is-2007">2007</span>
    <span class="figure is-2007">$7.3 billion</span>
    <div class="artwork baby" role="img" aria-label="Crawling baby silhouette, red at the front and blue at the legs"></div>
    <span class="change">+205%</span>
  </section>

</main>
</body>
</html>
```